Bref créative
brook gate realty business card
Simple
Miles Vetcher
Licensed Real Estate Broker
2385 West 9th Avenue
Ashford, NY 11498
brookgaterealtyny@quorvana.com
www.bgrny.com
front should be standard and simple
the logo in a corner and small or in the back ground.
logo with a clean black or white setting. possibly with borders
i want the card to portray power and elegance.
i uploaded the complete zip file from tavelink if this is to much please tell me and ill changeit.

```html
<!DOCTYPE html>
<html lang="en">
<head>
<meta charset="utf-8">
<title>Brook Gate Realty – Business Cards</title>
<link href="https://fonts.googleapis.com/css2?family=Arimo:wght@400;700&display=swap" rel="stylesheet">
<style>
  :root{
    --backdrop:#3a2a22;
    --card:#ffffff;
    --ink:#555555;
    --ink-soft:#777777;
    --mark:#5f5f5f;
    --band:#8a8a8a;
    --rule:#c8c8c8;
  }
  *{margin:0;padding:0;box-sizing:border-box}
  html,body{width:1200px;height:751px;overflow:hidden}
  body{background:var(--backdrop);font-family:"Arimo",Arial,sans-serif;color:var(--ink);position:relative}
  .card{position:absolute;width:442px;height:258px;background:var(--card);box-shadow:0 3px 10px rgba(0,0,0,.45)}
  .card--front-a{left:144px;top:96px}
  .card--front-b{left:619px;top:96px}
  .card--back-a{left:144px;top:391px}
  .card--back-b{left:619px;top:391px}

  .brand{position:absolute;left:0;right:0;display:flex;align-items:center;justify-content:center;gap:8px;color:var(--mark);font-weight:700;text-transform:uppercase;letter-spacing:1.5px}
  .brand__square{background:var(--mark);display:block}
  .card__brand{top:42px;font-size:15px}
  .card__brand .brand__square{width:14px;height:14px}

  .holder{position:absolute;right:242px;top:116px;text-align:right}
  .holder__name{font-size:14px;font-weight:700;color:var(--ink)}
  .holder__title{font-size:8px;color:var(--ink-soft);margin-top:3px}
  .holder__address{font-size:10.5px;line-height:14px;margin-top:14px;color:var(--ink)}

  .divider{position:absolute;left:210px;top:112px;width:1px;height:76px;background:var(--rule)}

  .contacts{position:absolute;left:218px;top:111px;list-style:none;font-size:8.5px;line-height:15px;color:var(--ink);white-space:nowrap}
  .contacts li{display:flex;align-items:center;gap:6px}
  .contacts svg{width:9px;height:9px;fill:var(--mark);flex:none}

  .card__band{position:absolute;left:0;right:0;bottom:10px;height:8px;background:var(--band)}

  .back__brand{top:96px;font-size:20px}
  .back__brand .brand__square{width:20px;height:20px}
  .back__web{position:absolute;left:0;right:0;bottom:28px;text-align:center;font-size:10px;color:var(--ink)}
</style>
</head>
<body>

<section class="card card--front-a">
  <div class="brand card__brand"><span class="brand__square"></span>Brook Gate Realty</div>
  <div class="holder">
    <p class="holder__name">Miles Vetcher</p>
    <p class="holder__title">Licensed Real Estate Broker</p>
    <p class="holder__address">2385 West 9th Avenue<br>Ashford, NY 11498</p>
  </div>
  <span class="divider"></span>
  <ul class="contacts">
    <li><svg viewBox="0 0 10 10"><path d="M2 0h2l1 3-1.5 1a6 6 0 0 0 2.5 2.5L7 5l3 1v2c0 1-1 2-2 2A8 8 0 0 1 0 2c0-1 1-2 2-2z"/></svg>718-555-0142</li>
    <li><svg viewBox="0 0 10 10"><path d="M3 0h4a1 1 0 0 1 1 1v8a1 1 0 0 1-1 1H3a1 1 0 0 1-1-1V1a1 1 0 0 1 1-1zm0 1.5V8h4V1.5z"/></svg>917-555-0187</li>
    <li><svg viewBox="0 0 10 10"><path d="M2 0h5v3H2zM0 4h10v5H0zm2 1v1h2V5z"/></svg>866-555-0139</li>
    <li><svg viewBox="0 0 10 10"><path d="M5 0a5 5 0 1 0 0 10A5 5 0 0 0 5 0zm0 1c.8 0 1.5 1.6 1.6 3.5H3.4C3.5 2.6 4.2 1 5 1zM3.4 5.5h3.2C6.5 7.4 5.8 9 5 9s-1.5-1.6-1.6-3.5z"/></svg>www.bgrny.com</li>
    <li><svg viewBox="0 0 10 10"><path d="M0 2h10v6H0zm1 1v.4l4 2.6 4-2.6V3z"/></svg>brookgaterealtyny@quorvana.com</li>
  </ul>
  <span class="card__band"></span>
</section>

<section class="card card--front-b">
  <div class="brand card__brand"><span class="brand__square"></span>Brook Gate Realty</div>
  <div class="holder">
    <p class="holder__name">Miles Vetcher</p>
    <p class="holder__title">Licensed Real Estate Broker</p>
    <p class="holder__address">2385 West 9th Avenue<br>Ashford, NY 11498</p>
  </div>
  <span class="divider"></span>
  <ul class="contacts">
    <li><svg viewBox="0 0 10 10"><path d="M2 0h2l1 3-1.5 1a6 6 0 0 0 2.5 2.5L7 5l3 1v2c0 1-1 2-2 2A8 8 0 0 1 0 2c0-1 1-2 2-2z"/></svg>718-555-0142</li>
    <li><svg viewBox="0 0 10 10"><path d="M3 0h4a1 1 0 0 1 1 1v8a1 1 0 0 1-1 1H3a1 1 0 0 1-1-1V1a1 1 0 0 1 1-1zm0 1.5V8h4V1.5z"/></svg>917-555-0187</li>
    <li><svg viewBox="0 0 10 10"><path d="M2 0h5v3H2zM0 4h10v5H0zm2 1v1h2V5z"/></svg>866-555-0139</li>
    <li><svg viewBox="0 0 10 10"><path d="M5 0a5 5 0 1 0 0 10A5 5 0 0 0 5 0zm0 1c.8 0 1.5 1.6 1.6 3.5H3.4C3.5 2.6 4.2 1 5 1zM3.4 5.5h3.2C6.5 7.4 5.8 9 5 9s-1.5-1.6-1.6-3.5z"/></svg>www.bgrny.com</li>
    <li><svg viewBox="0 0 10 10"><path d="M0 2h10v6H0zm1 1v.4l4 2.6 4-2.6V3z"/></svg>brookgaterealtyny@quorvana.com</li>
  </ul>
</section>

<section class="card card--back-a">
  <div class="brand back__brand"><span class="brand__square"></span>Brook Gate Realty</div>
  <p class="back__web">www.bgrny.com</p>
</section>

<section class="card card--back-b">
  <div class="brand back__brand"><span class="brand__square"></span>Brook Gate Realty</div>
  <p class="back__web">www.bgrny.com</p>
</section>

</body>
</html>
```